Austrian finance und insurance broker needs business card design

We Need a serious looking Design for Business Card. we consult private and corporates customers in finance and insurance questions. the final design should express security and experience. We consult customers in questions of loans, Investments and insurance and have a wide range of Banks to offer. We compare several offers and select the best for our customers.

Target Market(s)

private and coporate customers with efforts in Money and insurance

Industry/Entity Type

Insurance Broker

Contact Information for Business Card

Bernhard Aigner
Geschäftsführer
staatl. geprüfter Vermögensberater und Versicherungsmakler
Tel: 0664 521 8409
office@der-brandl.at
www.der-brandl.at
Leopold Hainz Gasse 14
2183 Melkstetten
GISA Nr. 48270315 u. 51736048 (backside)

Font styles to use
Serif
Sans Serif

Requirements
Must have
• logo (designcrowd zip) and all Details
Nice to have
• makler logo design, maybe a 2 coloured Version is possible

```html
<!DOCTYPE html>
<html lang="de">
<head>
<meta charset="utf-8">
<title>Visitenkarte – Aigner Vermögensberatung GmbH</title>
<link href="https://fonts.googleapis.com/css2?family=Arimo:wght@400;700&display=swap" rel="stylesheet">
<style>
  :root {
    --page: #ffffff;
    --frame: #111111;
    --brand-blue: #1f45ff;
    --slate: #4a5258;
    --ink: #111111;
    --metal-light: #eef2f7;
    --metal-mid: #c9d2dc;
    --metal-dark: #7d8ba3;
  }
  * { box-sizing: border-box; margin: 0; padding: 0; }
  html, body { width: 1020px; height: 1200px; overflow: hidden; background: var(--page); }
  body { font-family: "Arimo", Arial, sans-serif; position: relative; }
  .sheet-frame {
    position: absolute; inset: 1px 1px 1px 1px;
    border: 1.5px solid var(--frame);
  }
  .card {
    position: absolute; width: 878px; height: 530px; overflow: hidden;
  }
  .card--front { left: 77px; top: 46px; }
  .card--back { left: 75px; top: 616px; }
  .card__surface {
    position: absolute; inset: 0;
    background:
      linear-gradient(90deg, rgba(255,255,255,0.35) 0%, rgba(255,255,255,0) 30%, rgba(255,255,255,0.25) 55%, rgba(0,0,0,0) 70%),
      linear-gradient(160deg, var(--metal-light) 0%, var(--metal-mid) 55%, var(--metal-dark) 100%);
  }
  .card__content { position: absolute; inset: 0; }

  /* Front */
  .brand {
    position: absolute; left: 172px; top: 192px;
    display: flex; align-items: center; gap: 22px;
  }
  .brand__dot {
    width: 40px; height: 40px; border-radius: 50%;
    background: var(--brand-blue); flex: none;
  }
  .brand__text { display: flex; flex-direction: column; gap: 6px; }
  .brand__name {
    font-weight: 700; font-size: 30px; color: var(--brand-blue);
    letter-spacing: 0.2px;
  }
  .brand__tagline {
    font-size: 21px; color: var(--slate); font-weight: 400;
  }

  /* Back */
  .person { position: absolute; left: 0; right: 0; top: 50px; text-align: center; color: var(--brand-blue); }
  .person__name {
    font-size: 47px; font-weight: 700; line-height: 1;
    text-decoration: underline; text-decoration-thickness: 2px; text-underline-offset: 5px;
  }
  .person__role { font-size: 26px; margin-top: 12px; line-height: 33px; }

  .contact { position: absolute; left: 0; right: 0; top: 265px; text-align: center; color: var(--ink); font-size: 26px; }
  .contact__line { display: flex; justify-content: center; align-items: center; gap: 10px; height: 33px; }
  .contact__icon { width: 20px; height: 20px; fill: var(--ink); }
  .address { position: absolute; left: 0; right: 0; top: 399px; text-align: center; color: var(--ink); font-size: 26px; line-height: 33px; }
</style>
</head>
<body>
  <div class="sheet-frame"></div>

  <section class="card card--front">
    <div class="card__surface" role="img" aria-label="Gebürstete Metalloberfläche in Silber und Blaugrau"></div>
    <div class="card__content">
      <div class="brand">
        <span class="brand__dot"></span>
        <div class="brand__text">
          <span class="brand__name">Aigner Vermögensberatung GmbH</span>
          <span class="brand__tagline">Finanzieren, Versichern, Vorsorgen</span>
        </div>
      </div>
    </div>
  </section>

  <section class="card card--back">
    <div class="card__surface" role="img" aria-label="Gebürstete Metalloberfläche in Silber und Blaugrau"></div>
    <div class="card__content">
      <div class="person">
        <h1 class="person__name">Bernhard Aigner</h1>
        <p class="person__role">Geschäftsführer<br>staatl. geprüfter Vermögensberater und Versicherungsmakler</p>
      </div>

      <div class="contact">
        <div class="contact__line">
          <svg class="contact__icon" viewBox="0 0 24 24" aria-hidden="true"><path d="M6.6 10.8a15.1 15.1 0 0 0 6.6 6.6l2.2-2.2a1 1 0 0 1 1-.25 11.4 11.4 0 0 0 3.6.57 1 1 0 0 1 1 1V20a1 1 0 0 1-1 1A17 17 0 0 1 3 4a1 1 0 0 1 1-1h3.5a1 1 0 0 1 1 1c0 1.25.2 2.45.57 3.57a1 1 0 0 1-.25 1z"/></svg>
          <span>0664 521 8409</span>
        </div>
        <div class="contact__line">
          <svg class="contact__icon" viewBox="0 0 24 24" aria-hidden="true"><path d="M2 5h20v14H2z M4 7v.4l8 5.6 8-5.6V7z" fill-rule="evenodd"/></svg>
          <span>office@der-brandl.at</span>
        </div>
        <div class="contact__line">
          <svg class="contact__icon" viewBox="0 0 24 24" aria-hidden="true" fill="none" stroke="#111" stroke-width="1.8"><circle cx="12" cy="12" r="9"/><path d="M3 12h18M12 3c3 3 3 15 0 18M12 3c-3 3-3 15 0 18M5 7.5h14M5 16.5h14"/></svg>
          <span>www.der-brandl.at</span>
        </div>
      </div>

      <p class="address">Leopold Hainz Gasse 14<br>2183 Melkstetten<br>GISA Nr. 48270315 u. 51736048</p>
    </div>
  </section>
</body>
</html>
```